Calloway Winery Wine Label Re-design

Calloway Winery is located in the Finger Lakes region of New York. The Calloway Family planted the first vineyards in 1979 and opened in 1986. We produce award winning premium, hand crafted estate grown wines. We are in the process of a wine label re-design across our entire line. We would like to have the new label 'pop' but still convey elegance and ultra-premium quality. We are open to all color and styles or a minimalist design.
The attached files contain our new logo and samples of our current label (marked current) with dimensions. Our labeler is limited to label shapes but does not necessarily to have to be die-cut(the top arch) like our current label.

Target Market(s)

Upper income quality wine drinkers

Colors

Designer to choose colors to be used in the design.

Requirements
Should not have
• Should not be a tranparent label

```html
<!DOCTYPE html>
<html lang="en">
<head>
<meta charset="utf-8">
<title>Calloway Winery – Chardonnay Label</title>
<link rel="stylesheet" href="https://fonts.googleapis.com/css2?family=Libre+Baskerville:wght@400;700&family=Didact+Gothic&display=swap">
<style>
  :root {
    --page-bg: #dce6f3;
    --label-blue: #0c46c9;
    --stroke-blue: #0a36a6;
    --frame-white: #ffffff;
    --accent-orange: #f4a321;
  }
  * { margin: 0; padding: 0; box-sizing: border-box; }
  html, body {
    width: 1200px;
    height: 1018px;
    overflow: hidden;
    background: var(--page-bg);
  }
  .canvas {
    position: relative;
    width: 1200px;
    height: 1018px;
  }
  .wine-label {
    position: absolute;
    left: 360px;
    top: 29px;
    width: 480px;
    height: 960px;
    overflow: hidden;
    background: var(--label-blue);
  }
  .brush-pattern {
    position: absolute;
    inset: 0;
    background:
      linear-gradient(125deg, transparent 0 18%, var(--stroke-blue) 18% 27%, transparent 27% 44%, var(--stroke-blue) 44% 52%, transparent 52% 70%, var(--stroke-blue) 70% 78%, transparent 78%);
    opacity: 0.55;
  }
  .label-panel {
    position: absolute;
    left: 62px;
    top: 235px;
    width: 356px;
    height: 506px;
    border: 3px solid var(--frame-white);
    background: var(--label-blue);
    color: var(--frame-white);
    text-align: center;
  }
  .brand-mark {
    position: absolute;
    left: 50%;
    top: 44px;
    width: 76px;
    height: 76px;
    margin-left: -38px;
  }
  .brand-name {
    position: absolute;
    left: 0;
    right: 0;
    top: 132px;
    font-family: "Libre Baskerville", serif;
    font-weight: 400;
    color: var(--frame-white);
    line-height: 1;
  }
  .brand-name .primary {
    display: block;
    font-size: 30px;
    letter-spacing: 8px;
    padding-left: 8px;
  }
  .brand-name .secondary {
    display: block;
    margin-top: 12px;
    font-size: 16px;
    letter-spacing: 14px;
    padding-left: 14px;
  }
  .varietal {
    position: absolute;
    left: 0;
    right: 0;
    top: 352px;
    font-family: "Libre Baskerville", serif;
    font-weight: 700;
    font-size: 26px;
    letter-spacing: 0.5px;
  }
  .estate-line {
    position: absolute;
    left: 0;
    right: 0;
    top: 394px;
    font-family: "Didact Gothic", sans-serif;
    font-size: 14px;
    letter-spacing: 1px;
    color: var(--accent-orange);
  }
  .vintage {
    position: absolute;
    left: 0;
    right: 0;
    top: 414px;
    font-family: "Libre Baskerville", serif;
    font-weight: 700;
    font-size: 24px;
  }
</style>
</head>
<body>
  <main class="canvas">
    <section class="wine-label">
      <div class="brush-pattern" role="img" aria-label="Painted blue brushstroke background pattern"></div>
      <div class="label-panel">
        <svg class="brand-mark" viewBox="0 0 76 76" aria-hidden="true">
          <circle cx="38" cy="38" r="35" fill="none" stroke="#ffffff" stroke-width="3"/>
        </svg>
        <h1 class="brand-name">
          <span class="primary">CALLOWAY</span>
          <span class="secondary">WINERY</span>
        </h1>
        <p class="varietal">CHARDONNAY</p>
        <p class="estate-line">ESTATE GROWN &amp; BOTTLED</p>
        <p class="vintage">2014</p>
      </div>
    </section>
  </main>
</body>
</html>
```